Riverbend Haven Home Care-Nursing Assessment Form

I am creating a Nursing Assessment Form (which is used to be an intake form for all new patients) for my new home care company, Riverbend Haven Home Care.

It is 15 pages and pretty comprehensive as this is a very regulated field. I have all the necessary content and information attached in the word document below. Now, I am seeking a designer to make it look professional, cohesive and easy to read/ follow.
In order for your Word Document Design to be selected, you must:

1. As mentioned previously, make it easy to read/follow. There should be enough spacing, room to write out all necessary notes, fill out check marks...etc...
2. It should look professional.
3. It should be attractive and eye pleasing. Attached you will find our logo-kindly incorporate it's style into the project as well. The logo should be placed on top of each page.
4. Lastly, we need a Word Document version AND PDF Fillable Option. The fillable PDF should Auto Fill for the Name and Start of Care (SOC) Date.

I have attached a sample form below as well. This is how I envision the finished project to look. Of course, I am open to other suggestions as look as it meets the aforementioned requirements.

Thank you! May the best man or woman win!
Our team looks forward to working with our designer on this project!

Industry/Entity Type

Home Health Care

Font styles to use
Sans Serif

Colors
0255a3
9bcb3c

Requirements
Must have
• Refer to Project Description above.
Nice to have
We must be given a Word Document Option and PDF Fillable Option.

```html
<!DOCTYPE html>
<html lang="en">
<head>
<meta charset="utf-8">
<title>Riverbend Haven Home Care – Initial Assessment Form</title>
<link href="https://fonts.googleapis.com/css2?family=Roboto:ital,wght@0,400;0,700;0,900;1,400&display=swap" rel="stylesheet">
<style>
:root{
  --brand-blue:#0255a3;
  --brand-green:#9bcb3c;
  --ink:#1d1d1d;
  --rule:#c9c9c9;
  --band:#efefef;
  --canvas:#ececec;
  --paper:#ffffff;
}
*{box-sizing:border-box;margin:0;padding:0}
html,body{width:1200px;height:4003px;overflow:hidden}
body{background:var(--canvas);font-family:"Roboto",Arial,sans-serif;color:var(--ink);position:relative}
.page{position:absolute;left:67px;width:1068px;height:1380px;background:var(--paper);box-shadow:0 2px 10px rgba(0,0,0,.12);padding:0 62px}
.page-one{top:1089px;padding-top:96px}
.page-two{top:2553px;padding-top:76px}
.brand{display:flex;flex-direction:column;align-items:center;gap:10px}
.brand-mark{width:64px;height:64px;border-radius:50%;background:var(--brand-green)}
.brand-name{font-size:18px;font-weight:700;color:var(--brand-blue);letter-spacing:.5px;text-transform:uppercase}
.form-title{margin-top:22px;text-align:center;font-size:29px;font-weight:900;line-height:34px;letter-spacing:1px}
.form-note{text-align:center;font-size:13.5px;line-height:17px;margin-top:6px;margin-bottom:14px}
table.section{width:100%;border-collapse:collapse;table-layout:fixed;font-size:13.5px;margin-bottom:18px}
table.section td{border:1px solid var(--rule);height:28.5px;padding:0 8px;vertical-align:middle}
table.section td.tall{height:47px}
table.section td.xtall{height:62px}
.label{font-weight:700}
.small-hint{font-weight:400;font-style:italic;font-size:10.5px}
.band td{background:var(--band)}
.blank td{height:28.5px}
.box{display:inline-block;width:10px;height:10px;border:1px solid #333;margin-right:6px;vertical-align:-1px}
.opt{margin-right:18px;white-space:nowrap}
.yn{width:70px}
.page-footer{position:absolute;left:76px;right:76px;bottom:50px;display:flex;justify-content:space-between;align-items:flex-end;font-size:10.5px}
.turn{font-style:italic}
.page-number{font-size:14px;position:relative;top:-26px}
</style>
</head>
<body>

<section class="page page-one">
  <header class="brand">
    <span class="brand-mark"></span>
    <span class="brand-name">Riverbend Haven Home Care</span>
  </header>
  <h1 class="form-title">RIVERBEND HAVEN HOME CARE<br>INITIAL ASSESSMENT FORM</h1>
  <p class="form-note">All questions contained in this questionnaire are strictly confidential<br>and will become part of your medical record.</p>

  <table class="section">
    <colgroup><col style="width:157px"><col style="width:265px"><col style="width:65px"><col style="width:150px"><col style="width:305px"></colgroup>
    <tr><td colspan="4"><span class="label">Name</span> <span class="small-hint">(Last, First, M.I.):</span></td><td class="label">SOC Date:</td></tr>
    <tr class="blank"><td colspan="5"></td></tr>
  </table>

  <table class="section" style="margin-top:-18px">
    <colgroup><col style="width:157px"><col style="width:265px"><col style="width:65px"><col style="width:225px"><col style="width:230px"></colgroup>
    <tr><td colspan="3" class="label">Patient’s Name:</td><td><span class="label">Gender:</span> <span class="box"></span>M &nbsp; <span class="box"></span>F</td><td class="label">Date:</td></tr>
    <tr><td colspan="3" class="label">Primary Diagnosis:</td><td colspan="2" class="label">Secondary Diagnosis:</td></tr>
    <tr><td colspan="3" class="label">Other Pertinent Diagnosis:</td><td colspan="2" class="label">PCP name:</td></tr>
    <tr><td colspan="5" class="label">Other Physician Name:</td></tr>
    <tr class="blank"><td colspan="5"></td></tr>
    <tr><td colspan="5"><span class="label" style="margin-right:40px">Prognosis:</span><span class="opt"><span class="box"></span>Poor</span><span class="opt"><span class="box"></span>Fair</span><span class="opt"><span class="box"></span>Good</span><span class="opt"><span class="box"></span>Excellent</span></td></tr>
  </table>

  <table class="section" style="margin-top:-18px">
    <colgroup><col style="width:157px"><col style="width:265px"><col style="width:260px"><col style="width:260px"></colgroup>
    <tr><td rowspan="2" class="label">Vital Signs:</td><td class="label">Height:</td><td class="label">Weight:</td><td class="label">Temp:</td></tr>
    <tr><td class="label">Pulse:</td><td class="label">Resp:</td><td class="label">B/P:</td></tr>
    <tr><td colspan="4" class="label">Allergies:</td></tr>
    <tr><td colspan="4" class="label xtall">Past Medical and Surgical History:</td></tr>
  </table>

  <table class="section">
    <colgroup><col style="width:490px"><col style="width:452px"></colgroup>
    <tr class="band"><td colspan="2" class="label">Support System:</td></tr>
    <tr><td colspan="2"><span class="label" style="display:inline-block;width:157px">Childhood illness:</span><span class="opt"><span class="box"></span>Married</span><span class="opt"><span class="box"></span>Not Married</span><span class="opt"><span class="box"></span>Single</span><span class="opt"><span class="box"></span>Divorced</span><span class="opt"><span class="box"></span>Divorced</span><span class="opt"><span class="box"></span>Widowed</span></td></tr>
    <tr><td colspan="2"><span class="label" style="display:inline-block;width:157px">Lives Alone:</span><span class="opt" style="margin-right:50px"><span class="box"></span>Yes</span><span class="opt"><span class="box"></span>No</span></td></tr>
    <tr><td colspan="2" class="label">Family Composition:</td></tr>
    <tr><td class="label">Legal Next of Kin:</td><td class="label">Telephone:</td></tr>
    <tr><td class="label">Address:</td><td class="label">E-mail:</td></tr>
    <tr><td rowspan="2" class="label">Is significant other able, available, capable and willing to care for patient?</td><td><span class="box"></span>Yes</td></tr>
    <tr><td><span class="box"></span>No</td></tr>
    <tr><td colspan="2" class="label">If No, explain:</td></tr>
    <tr><td colspan="2" class="label tall">Educational Needs of Patient/Family:</td></tr>
  </table>

  <table class="section">
    <colgroup><col><col><col><col></colgroup>
    <tr class="band"><td colspan="4" class="label">Environment:</td></tr>
    <tr><td><span class="box"></span>Private Home</td><td><span class="box"></span>Apartment</td><td><span class="box"></span>Elevator</td><td><span class="box"></span>Walkup Apartment</td></tr>
  </table>

  <table class="section">
    <colgroup><col style="width:302px"><col style="width:326px"><col style="width:314px"></colgroup>
    <tr class="band"><td colspan="3" class="label">Safety Hazards in the Home:</td></tr>
    <tr><td><span class="box"></span>Sound structure</td><td><span class="box"></span>Safe Placement of Cords, Rugs and Furniture</td><td><span class="box"></span>Adequate Heating and Ventilation</td></tr>
    <tr><td><span class="box"></span>Adequate Cooking facility</td><td><span class="box"></span>Adequate Plumbing/Sanitation/ Running Water</td><td><span class="box"></span>Safe Gas/Electric Appliances</td></tr>
    <tr><td><span class="box"></span>Grounded Plug for Equipment</td><td><span class="box"></span>Enough Electrical Outlets for Equipment</td><td><span class="box"></span>Safe storage for Supplies/Equipment/Meds?</td></tr>
  </table>

  <footer class="page-footer"><span class="turn">Please turn to next page</span><span class="page-number">1</span></footer>
</section>

<section class="page page-two">
  <table class="section">
    <colgroup><col style="width:302px"><col style="width:326px"><col style="width:314px"></colgroup>
    <tr><td><span class="box"></span>Exits Free of Obstruction</td><td><span class="box"></span>Working smoke detectors?</td><td><span class="box"></span>Fire extinguisher in home?</td></tr>
    <tr><td class="tall"><span class="box"></span>Infestations of pests?</td><td><span class="box"></span>Neighborhood safe?</td><td><span class="box"></span>Working Adequate Sleeping Arrangement<br><span style="margin-left:17px">Telephone in the Home</span></td></tr>
    <tr><td colspan="3" class="label">Comments:</td></tr>
  </table>

  <table class="section">
    <colgroup><col style="width:470px"><col style="width:472px"></colgroup>
    <tr class="band"><td colspan="2" class="label">Caregiver’s Contact Information:</td></tr>
    <tr><td colspan="2" class="label">Name:</td></tr>
    <tr><td colspan="2" class="label">Telephone:</td></tr>
    <tr><td class="label">Address:</td><td class="label">E-mail:</td></tr>
    <tr><td colspan="2" class="label">Days / Time Available:</td></tr>
  </table>

  <table class="section">
    <colgroup><col><col class="yn"><col class="yn"></colgroup>
    <tr class="band"><td colspan="3" class="label">Caregivers Ability to Assist Patient / Able to Provide:</td></tr>
    <tr><td class="label">Personal Care:</td><td><span class="box"></span>Yes</td><td><span class="box"></span>No</td></tr>
    <tr><td class="label">Mobility:</td><td><span class="box"></span>Yes</td><td><span class="box"></span>No</td></tr>
    <tr><td class="label">Prepare/Serve Meals:</td><td><span class="box"></span>Yes</td><td><span class="box"></span>No</td></tr>
    <tr><td class="label">Maintain Safe/Clean Environment:</td><td><span class="box"></span>Yes</td><td><span class="box"></span>No</td></tr>
    <tr><td class="label">Perform/ Assist with Procedures:</td><td><span class="box"></span>Yes</td><td><span class="box"></span>No</td></tr>
    <tr><td class="label">Caregiver has capacity to learn therapeutic regimen:</td><td><span class="box"></span>Yes</td><td><span class="box"></span>No</td></tr>
    <tr><td colspan="3" class="label">Comments:</td></tr>
  </table>

  <table class="section">
    <colgroup><col><col class="yn"><col class="yn"></colgroup>
    <tr class="band"><td class="label">Are There Any Signs of Abuse or Neglect from Family or Caregiver?</td><td><span class="box"></span>Yes</td><td><span class="box"></span>No</td></tr>
    <tr><td colspan="3" class="label">If Yes, describe:</td></tr>
    <tr class="blank"><td colspan="3"></td></tr>
    <tr class="blank"><td colspan="3"></td></tr>
  </table>

  <table class="section">
    <colgroup><col><col class="yn"><col class="yn"></colgroup>
    <tr class="band"><td colspan="3" class="label">Advanced Directives:</td></tr>
    <tr><td class="label">Patient has a Living Will</td><td><span class="box"></span>Yes</td><td><span class="box"></span>No</td></tr>
    <tr><td class="label">Health Care Proxy</td><td><span class="box"></span>Yes</td><td><span class="box"></span>No</td></tr>
    <tr><td colspan="3"><span class="label" style="display:inline-block;width:240px">Special Provisions Included:</span><span class="opt"><span class="box"></span>DNR</span><span class="opt"><span class="box"></span>DNI</span><span class="opt"><span class="box"></span>No Mech</span></td></tr>
    <tr><td colspan="3"><span class="label" style="display:inline-block;width:240px">Ventilation:</span><span class="opt"><span class="box"></span>Med. Support Only</span><span class="opt"><span class="box"></span>No Feeding Tubes</span></td></tr>
    <tr><td class="label">Copies of Documentation Attached</td><td><span class="box"></span>Yes</td><td><span class="box"></span>No</td></tr>
    <tr><td colspan="3" class="label">Other:</td></tr>
  </table>

  <table class="section">
    <colgroup><col><col class="yn"><col class="yn"></colgroup>
    <tr class="band"><td colspan="3" class="label">Nutritional:</td></tr>
    <tr><td colspan="3" class="label">Diet:</td></tr>
    <tr><td colspan="3" class="label">Meals Prepared By:</td></tr>
    <tr><td colspan="3" class="label">Meals Patterns/Tolerance/Restrictions:</td></tr>
    <tr><td class="label">Compliance:</td><td><span class="box"></span>Yes</td><td><span class="box"></span>No</td></tr>
  </table>

  <table class="section">
    <colgroup><col style="width:630px"><col style="width:312px"></colgroup>
    <tr class="band"><td class="label">Statement:</td><td class="label">Value:</td></tr>
    <tr><td>1. I have an illness or condition that made me change the kind and/or amount of food I eat-</td><td>2</td></tr>
    <tr><td>2. I eat fewer than two meals per day</td><td>3</td></tr>
    <tr><td>3. I do not eat fruits, vegetables or milk products</td><td>2</td></tr>
    <tr><td>4. I have three of more drinks of beer, liquor or wine almost every day</td><td>2</td></tr>
  </table>

  <footer class="page-footer"><span class="turn">Please turn to next page</span><span class="page-number">2</span></footer>
</section>

</body>
</html>
```